Olive Oil Label Needs Graphic Designs

We need two sister label designs for 500ml bottles for our new brand "Casa Lumen". Casa Lumen is a high-end olive oil from Baeza, Spain which will be sold in the US. The oil will be produced from both Arbequina olives and Picual olives. Therefore, envisioning the same design just a different color scheme for the different labels.
The label should have the following characteristics; clean and simple, stand-out from mainstream labels, be eye-catching, give perception of high-end / high-quality.
Our current thinking of what we want (but please let your creative juices flow); lighter background, to be more eye catching, graphics of and olive, a olive branch or olive tree.
Text which should appear on the label are (not necessarily in this order);
Casa Lumen
Extra Virgin Olive Oil
Family Reserve
Arbequina (One design)
Picual (Second design)
The label should be about 3 inches wide and 5.5 inches in height.

```html
<!DOCTYPE html>
<html lang="en">
<head>
<meta charset="utf-8">
<title>Casa Lumen – Olive Oil Labels</title>
<link rel="stylesheet" href="https://fonts.googleapis.com/css2?family=Barlow+Condensed:wght@300;400;500;600&display=swap">
<style>
  :root {
    --charcoal: #333333;
    --olive: #958c34;
    --olive-light: #b3a83c;
    --leaf: #66784f;
    --leaf-light: #a9ad82;
    --navy: #1f2a38;
    --navy-light: #3a4a5c;
    --paper: #ffffff;
    --ink-light: #f2f2f2;
    --ink-dark: #4a4a4a;
  }
  * { margin: 0; padding: 0; box-sizing: border-box; }
  html, body {
    width: 1200px; height: 980px; overflow: hidden;
    background: var(--paper);
    font-family: "Barlow Condensed", sans-serif;
  }
  .canvas { position: relative; width: 1200px; height: 980px; }

  .label {
    position: absolute; top: 0; width: 534px; height: 978px; overflow: hidden;
  }
  .label--arbequina {
    left: 0; background: var(--charcoal); color: var(--ink-light);
    --accent: var(--olive); --fruit-a: var(--olive-light); --fruit-b: var(--olive);
  }
  .label--picual {
    left: 665px; width: 535px; height: 980px; background: var(--paper); color: var(--ink-dark);
    border: 2px solid var(--charcoal);
    --accent: var(--navy); --fruit-a: var(--navy-light); --fruit-b: var(--navy);
  }
  .label--picual .label__inner { position: absolute; left: -2px; top: -2px; right: -2px; bottom: -2px; }
  .label--arbequina .label__inner { position: absolute; inset: 0; }

  .label__category {
    position: absolute; left: 50px; top: 62px;
    font-weight: 300; font-size: 68px; line-height: 70px; letter-spacing: -1px;
    text-transform: uppercase;
  }
  .label__rule {
    position: absolute; left: 50px; top: 234px; width: 178px; height: 9px;
    background: var(--accent);
  }
  .label__brand {
    position: absolute; left: 48px; top: 266px;
    font-weight: 600; font-size: 124px; line-height: 118px; letter-spacing: -1px;
    text-transform: uppercase;
  }

  .label__band {
    position: absolute; left: 0; top: 573px; width: 100%; height: 84px;
    background: var(--accent);
  }
  .label__variety {
    position: absolute; left: 50px; top: 582px;
    font-weight: 500; font-size: 64px; line-height: 64px;
    color: var(--ink-light); text-transform: uppercase;
  }
  .label__illustration {
    position: absolute; right: 0; top: 336px; width: 222px; height: 372px;
  }
  .label__reserve {
    position: absolute; left: 0; width: 100%; top: 750px;
    font-weight: 300; font-size: 46px; line-height: 52px;
    text-transform: uppercase; text-align: center;
  }
  .label__volume {
    position: absolute; left: 0; width: 100%; top: 846px;
    font-weight: 500; font-size: 52px; line-height: 56px;
    text-align: center;
  }
</style>
</head>
<body>
<main class="canvas">
  <section class="label label--arbequina">
    <div class="label__inner">
      <p class="label__category">Extra Virgin<br>Olive Oil</p>
      <div class="label__rule"></div>
      <h1 class="label__brand">Casa<br>Lumen</h1>
      <div class="label__band"></div>
      <svg class="label__illustration" viewBox="0 0 222 372" role="img" aria-label="Olive branch with two green Arbequina olives">
        <defs>
          <linearGradient id="leaves-green" x1="0" y1="0" x2="0" y2="1">
            <stop offset="0" stop-color="var(--leaf)"/>
            <stop offset="1" stop-color="var(--leaf-light)"/>
          </linearGradient>
          <linearGradient id="fruit-green" x1="0" y1="0" x2="0" y2="1">
            <stop offset="0" stop-color="var(--olive-light)"/>
            <stop offset="1" stop-color="var(--olive)"/>
          </linearGradient>
        </defs>
        <rect x="112" y="0" width="110" height="200" rx="50" fill="url(#leaves-green)"/>
        <rect x="0" y="180" width="222" height="192" rx="80" fill="url(#fruit-green)"/>
      </svg>
      <p class="label__variety">Arbequina</p>
      <p class="label__reserve">Family Reserve</p>
      <p class="label__volume">500ml</p>
    </div>
  </section>

  <section class="label label--picual">
    <div class="label__inner">
      <p class="label__category">Extra Virgin<br>Olive Oil</p>
      <div class="label__rule"></div>
      <h1 class="label__brand">Casa<br>Lumen</h1>
      <div class="label__band"></div>
      <svg class="label__illustration" viewBox="0 0 222 372" role="img" aria-label="Olive branch with two dark Picual olives">
        <defs>
          <linearGradient id="leaves-navy" x1="0" y1="0" x2="0" y2="1">
            <stop offset="0" stop-color="var(--leaf)"/>
            <stop offset="1" stop-color="var(--leaf-light)"/>
          </linearGradient>
          <linearGradient id="fruit-navy" x1="0" y1="0" x2="0" y2="1">
            <stop offset="0" stop-color="var(--navy-light)"/>
            <stop offset="1" stop-color="var(--navy)"/>
          </linearGradient>
        </defs>
        <rect x="112" y="0" width="110" height="200" rx="50" fill="url(#leaves-navy)"/>
        <rect x="0" y="180" width="222" height="192" rx="80" fill="url(#fruit-navy)"/>
      </svg>
      <p class="label__variety">Picual</p>
      <p class="label__reserve">Family Reserve</p>
      <p class="label__volume">500ml</p>
    </div>
  </section>
</main>
</body>
</html>
```